Digital Billboard

we want our Fern & Pebble logo really big
Use a really bold font for the wording as it's on a billboard on the highway

Fern & Pebble Logo
perhaps on left hand side really large then have a slanting line and a different colour background for the other side.
include kindy approved program
Wording BELOW- have the Wollara Creek text really bold

Join our
WOLLARA CREEK
COMMUNITY
6 weeks to 6 years

PROGRESSIVE I INNOVATIVE I HOLISTIC
fernandpebble.edu.au

Use one image, I have attached multiple to choose from so you can choose something that works with your design
specs- 1224 W × 324 H px JPEG

Target Market(s)

families

Industry/Entity Type

childcare

Requirements
Must have
• eye catching

```html
<!DOCTYPE html>
<html lang="en">
<head>
<meta charset="utf-8">
<title>Fern &amp; Pebble – Wollara Creek Billboard</title>
<link rel="stylesheet" href="https://fonts.googleapis.com/css2?family=Montserrat:wght@900&family=Oswald:wght@600;700&family=Quicksand:wght@700&display=swap">
<style>
  :root{
    --stage:#e7e7e8;
    --blue:#0a8dd0;
    --blue-deep:#0a6aa8;
    --yellow:#f6cd1c;
    --amber:#f9bf4b;
    --navy:#1d2a4e;
    --white:#ffffff;
    --badge-fill:#fbe39a;
    --badge-edge:#3f9cc4;
  }
  *{margin:0;padding:0;box-sizing:border-box}
  html,body{width:1200px;height:459px;overflow:hidden;background:var(--stage)}
  .billboard{position:absolute;left:0;top:70px;width:1200px;height:318px;overflow:hidden;background:var(--blue)}
  .billboard__shapes{position:absolute;inset:0}
  .join-tab{position:absolute;left:42px;top:8px;font:700 31px/1 'Oswald',sans-serif;color:var(--navy)}
  .headline{position:absolute;left:34px;top:78px;font:900 63px/57px 'Montserrat',sans-serif;color:var(--white);letter-spacing:.5px;text-shadow:0 3px 8px rgba(0,40,80,.35)}
  .age-pill{position:absolute;left:475px;top:141px;width:161px;height:47px;border-radius:8px;background:var(--yellow);font:700 20px/47px 'Oswald',sans-serif;color:var(--navy);text-align:center}
  .rule{position:absolute;left:33px;top:214px;width:101px;height:4px;border-radius:2px;background:var(--yellow)}
  .values{position:absolute;left:33px;top:234px;font:600 26px/1 'Oswald',sans-serif;color:var(--white);letter-spacing:.2px}
  .values .sep{color:var(--yellow);padding:0 6px}
  .web{position:absolute;left:32px;top:283px;display:flex;align-items:center;gap:16px}
  .web__url{font:700 16px/1 'Quicksand',sans-serif;color:var(--navy);letter-spacing:5.2px}
  .brand{position:absolute;left:1040px;top:190px;width:150px;text-align:center;font:900 29px/31px 'Montserrat',sans-serif;color:var(--yellow)}
</style>
</head>
<body>
<main class="billboard">
  <svg class="billboard__shapes" width="1200" height="318" viewBox="0 0 1200 318">
    <defs>
      <radialGradient id="blueGlow" cx="0.4" cy="0.6" r="0.7">
        <stop offset="0" stop-color="#0b9ad9"/><stop offset="1" stop-color="#0a6aa8"/>
      </radialGradient>
      <linearGradient id="photoTones" x1="0" y1="0" x2="1" y2="1">
        <stop offset="0" stop-color="#9fd3ea"/><stop offset=".45" stop-color="#f1a9c4"/><stop offset=".75" stop-color="#e9c8c3"/><stop offset="1" stop-color="#b9c4c8"/>
      </linearGradient>
      <linearGradient id="amberFade" x1="0" y1="0" x2="0" y2="1">
        <stop offset="0" stop-color="#f7c23d"/><stop offset="1" stop-color="#fcc55c"/>
      </linearGradient>
      <linearGradient id="roundPhoto" x1="0" y1="0" x2="1" y2="1">
        <stop offset="0" stop-color="#5a4b58"/><stop offset=".5" stop-color="#9bc6de"/><stop offset="1" stop-color="#c56f8a"/>
      </linearGradient>
    </defs>
    <rect class="panel-blue" width="1200" height="318" fill="url(#blueGlow)"/>
    <polygon class="photo-panel" points="739,0 1200,0 1200,318 899,318" fill="url(#photoTones)" role="img" aria-label="Photograph of a smiling toddler in a colourful classroom"/>
    <polygon class="amber-triangle" points="527,318 790,150 899,318" fill="url(#amberFade)"/>
    <circle class="logo-disc" cx="1130" cy="300" r="150" fill="var(--blue)"/>
    <circle cx="748" cy="118" r="80" fill="#cfe3ee"/>
    <circle class="round-photo" cx="748" cy="118" r="76" fill="url(#roundPhoto)" role="img" aria-label="Photograph of a child with face paint playing at a community event"/>
    <rect class="approval-badge" x="659" y="215" width="131" height="84" rx="6" fill="var(--badge-fill)" stroke="var(--badge-edge)" stroke-width="3"/>
    <polygon class="join-band" points="0,0 177,0 157,58 0,58" fill="var(--yellow)"/>
    <polygon points="177,0 181,0 161,58 157,58" fill="var(--white)"/>
    <polygon class="web-band" points="0,279 304,279 319,318 0,318" fill="var(--yellow)"/>
  </svg>

  <div class="join-tab">Join our</div>
  <h1 class="headline">WOLLARA CREEK<br>COMMUNITY</h1>
  <div class="age-pill">6 WEEKS - 6 YEARS</div>
  <div class="rule"></div>
  <p class="values">PROGRESSIVE<span class="sep">I</span>INNOVATIVE<span class="sep">I</span>HOLISTIC</p>
  <div class="web">
    <svg width="18" height="18" viewBox="0 0 18 18" aria-hidden="true">
      <circle cx="9" cy="9" r="9" fill="var(--navy)"/>
      <g fill="none" stroke="var(--yellow)" stroke-width="1.1">
        <circle cx="9" cy="9" r="5.5"/><ellipse cx="9" cy="9" rx="2.3" ry="5.5"/><line x1="3.5" y1="9" x2="14.5" y2="9"/>
      </g>
    </svg>
    <span class="web__url">fernandpebble.edu.au</span>
  </div>
  <div class="brand">Fern &amp;<br>Pebble</div>
</main>
</body>
</html>
```